Dolsemk Business Cards

Business cards for real estate
Target Market(s)
Real estate
Industry/Entity Type
Real Estate Agent
Font styles to use
Serif
Requirements
Must have
- Photo and logo

```html
<!DOCTYPE html>
<html lang="en">
<head>
<meta charset="utf-8">
<title>Dolsemk Realty Business Card</title>
<link href="https://fonts.googleapis.com/css2?family=Cinzel:wght@400&family=Roboto:wght@400;500&display=swap" rel="stylesheet">
<style>
  :root {
    --page: #e9e6e1;
    --crimson: #a51d3a;
    --gold: #dcc08e;
    --gold-deep: #c9a56a;
    --paper: #ffffff;
    --ink-light: #ffffff;
    --ink-soft: #f5e6ea;
  }
  * { margin: 0; padding: 0; box-sizing: border-box; }
  html, body { width: 1200px; height: 1022px; overflow: hidden; }
  body {
    background: var(--page);
    font-family: "Roboto", Arial, sans-serif;
    position: relative;
  }
  .business-card {
    position: absolute;
    left: 100px; top: 226px;
    width: 1000px; height: 570px;
    border-radius: 34px;
    overflow: hidden;
    background: var(--paper);
    box-shadow: 0 10px 30px rgba(0,0,0,0.18);
  }
  .card-art { position: absolute; inset: 0; }
  .brand {
    position: absolute;
    left: 60px; top: 56px;
    display: flex; align-items: center; gap: 22px;
    color: var(--ink-light);
  }
  .brand-mark {
    width: 64px; height: 64px;
    border-radius: 50%;
    background: var(--ink-light);
    opacity: 0.9;
  }
  .brand-name {
    font-family: "Cinzel", Georgia, serif;
    font-weight: 400;
    font-size: 44px;
    line-height: 1;
    letter-spacing: 2px;
  }
  .brand-name span { display: block; font-size: 34px; letter-spacing: 9px; margin-top: 6px; }
  .agent {
    position: absolute;
    left: 150px; top: 216px;
    color: var(--ink-light);
  }
  .agent-name {
    font-weight: 500;
    font-size: 32px;
    letter-spacing: 1px;
    text-transform: uppercase;
    white-space: nowrap;
  }
  .agent-role { font-size: 19px; margin-top: 4px; color: #fff8ee; }
  .contact {
    position: absolute;
    left: 150px; top: 344px;
    list-style: none;
    color: var(--ink-soft);
    font-size: 23px;
    line-height: 34px;
    white-space: nowrap;
  }
  .contact li { position: relative; }
  .contact svg {
    position: absolute; left: -30px; top: 10px;
    width: 16px; height: 16px;
  }
</style>
</head>
<body>
  <article class="business-card">
    <svg class="card-art" viewBox="0 0 1000 570" width="1000" height="570">
      <defs>
        <linearGradient id="portraitTone" x1="0" y1="0" x2="1" y2="1">
          <stop offset="0" stop-color="#f4f4f4"/>
          <stop offset="0.45" stop-color="#d9d2cc"/>
          <stop offset="1" stop-color="#1c2230"/>
        </linearGradient>
      </defs>
      <rect x="0" y="0" width="1000" height="570" fill="var(--crimson)"/>
      <rect x="0" y="190" width="1000" height="118" fill="var(--gold)"/>
      <rect x="720" y="0" width="280" height="570" fill="var(--paper)"/>
      <rect x="640" y="308" width="360" height="262" fill="var(--paper)"/>
      <circle cx="800" cy="190" r="304" fill="var(--gold-deep)"/>
      <circle cx="800" cy="190" r="296" fill="var(--paper)"/>
      <circle cx="800" cy="190" r="290" fill="url(#portraitTone)" role="img" aria-label="Portrait photo of the agent in a dark suit and blue tie"/>
    </svg>

    <div class="brand">
      <div class="brand-mark"></div>
      <div class="brand-name">DOLSEMK<span>REALTY</span></div>
    </div>

    <div class="agent">
      <h1 class="agent-name">Daniel Rourke</h1>
      <p class="agent-role">Director</p>
    </div>

    <ul class="contact">
      <li>214b Harlow Street,</li>
      <li>Eastbridge, NZ, 8042</li>
      <li><svg viewBox="0 0 16 16"><path d="M3 1l3 3-2 2c1 2 3 4 5 5l2-2 3 3-2 3C6 14 2 10 1 3z" fill="#fff"/></svg>(555) 310-4872</li>
      <li><svg viewBox="0 0 16 16"><rect x="1" y="3" width="14" height="10" rx="1" fill="none" stroke="#fff" stroke-width="1.6"/><path d="M1 4l7 5 7-5" fill="none" stroke="#fff" stroke-width="1.6"/></svg>info@dolsemkrealty.com</li>
      <li><svg viewBox="0 0 16 16"><circle cx="8" cy="8" r="6.5" fill="none" stroke="#fff" stroke-width="1.5"/><path d="M1.5 8h13M8 1.5c-3 3-3 10 0 13M8 1.5c3 3 3 10 0 13" fill="none" stroke="#fff" stroke-width="1.2"/></svg>www.dolsemkrealty.com</li>
    </ul>
  </article>
</body>
</html>
```